Jewelry Shop Needs a Cash Coupon Design

Mabel’s Nook is a Hong Kong based fine jewelry brand. We need a Cash Coupon for marketing promotion use.
Size: 1/6 A4 Size (want to print 6 pieces in one A4 paper)
Font Content:
1. Company Logo
2. HKD 500
3. 现金券 Cash Voucher
4. Jewelry Willow Loft
5. 香港九龍油麻地林木里18-26號福安大廈5樓
5/F , Fook On Building, 18-26 Linwood Lane, YMT, HK
T: +852 29480517 F: +852 29480519 M: info@mabelsnook.co
Back Content:
1. Terms and Conditions
Mabel’s Nook philosophy is a jewelry icon of young, creative, trendy, fashionable, stylish, energetic, and elegant. For Mabel’s Nook, jewelry is one collection of artworks, the most important items in personal life.
Marketing

```html
<!DOCTYPE html>
<html lang="en">
<head>
<meta charset="utf-8">
<title>Mabel’s Nook Cash Coupon – Terms Sheet</title>
<link rel="stylesheet" href="https://fonts.googleapis.com/css2?family=Noto+Serif+TC:wght@600&family=Roboto+Slab:wght@800&display=swap">
<style>
:root{
  --gold-deep:#7d6b17;
  --gold-mid:#c4b038;
  --gold-bright:#f4ea78;
  --gold-edge:#6e5e12;
  --ink:#231d02;
  --divider:#5a4b0c;
}
*{margin:0;padding:0;box-sizing:border-box}
html,body{width:848px;height:1200px;overflow:hidden;background:var(--gold-deep)}
.sheet{width:848px;height:1200px;display:flex;flex-direction:column}
.coupon-back{
  height:200px;
  border-bottom:1px solid var(--divider);
  background:linear-gradient(180deg,var(--gold-deep) 0%,var(--gold-mid) 30%,var(--gold-bright) 68%,#e9dc62 85%,var(--gold-edge) 100%);
  color:var(--ink);
  text-align:center;
  padding-top:6px;
}
.terms-zh{font-family:"Noto Serif TC",serif;font-weight:600;font-size:7.4px;line-height:9px}
.terms-zh .title{margin-bottom:0}
.terms-en{font-family:"Roboto Slab",Georgia,serif;font-weight:800;font-size:7.4px;line-height:9px;margin-top:12px}
.terms-en .title{margin-bottom:0}
</style>
</head>
<body>
<main class="sheet">

<section class="coupon-back">
  <div class="terms-zh">
    <p class="title">現金券條款及細則</p>
    <p>1. 此現金券為本公司(Mabel’s Nook)的購物現金回贈，每次於本公司購物滿港幣$5000或以上(以發票上所示的購物金額為準，並需要在同一張發票內計算)，並需要成功申請成為本公司VIP會員，方可獲贈HK$500 現金回贈。</p>
    <p>2. 每位合格客戶每次購物滿港幣$5000或以上可使用一張現金回贈券一張，購物滿港幣$10000或以上可使用兩張現金回贈券，如此類推，不設上限，多買多回贈。</p>
    <p>3. 現金券的使用細則須受本公司的相關條款限制，現金券如有遺失或損毀，本公司(Mabel’s Nook)概不補發或更換現金券，亦不會<br>承擔任何責任。</p>
    <p>4. 本公司保留隨時修改、暫停或取消以上優惠及其條款及細則的權利，毋須事先通知。如有任何爭議，本公司將保留最終決定權。</p>
    <p>5. 如此條款及細則的中、英文版有所差異，一概以中文版為準。</p>
  </div>
  <div class="terms-en">
    <p class="title">The Cash Coupon Terms and Conditions</p>
    <p>1.&nbsp; The cash coupon is the cash reward of shopping in Mabel’s Nook. Those consumers having purchased $5000 or above in our company every time (be subject to the shopping<br>amount shown on the invoice, calculated on the same invoice as required), and successfully applied for the VIP members of our company, will be presented with HK$500 cash reward.</p>
    <p>2.&nbsp; Each qualified client can use one cash coupon if he purchases for HK$5000 or above every time; for HK$10000 or above can use<br>two cash coupons and so on, no cap, purchase more and more in return.</p>
    <p>3.&nbsp; The using details of cash coupon must be subjected to the company’s related terms restrictions. Mabel’s Nook will not reissue or exchange cash<br>coupons in case of any loss or defacement, or undertake any responsibility.</p>
    <p>4.&nbsp; This company reserves the right to modify, suspend or cancel the above privileges, terms and conditions, without prior notice. In case of disputes, t<br>his company reserves the right to make final decision.</p>
    <p>5. In case of any difference between the Chinese and English versions in the terms and conditions, the Chinese version shall prevail.</p>
  </div>
</section>

<section class="coupon-back">
  <div class="terms-zh">
    <p class="title">現金券條款及細則</p>
    <p>1. 此現金券為本公司(Mabel’s Nook)的購物現金回贈，每次於本公司購物滿港幣$5000或以上(以發票上所示的購物金額為準，並需要在同一張發票內計算)，並需要成功申請成為本公司VIP會員，方可獲贈HK$500 現金回贈。</p>
    <p>2. 每位合格客戶每次購物滿港幣$5000或以上可使用一張現金回贈券一張，購物滿港幣$10000或以上可使用兩張現金回贈券，如此類推，不設上限，多買多回贈。</p>
    <p>3. 現金券的使用細則須受本公司的相關條款限制，現金券如有遺失或損毀，本公司(Mabel’s Nook)概不補發或更換現金券，亦不會<br>承擔任何責任。</p>
    <p>4. 本公司保留隨時修改、暫停或取消以上優惠及其條款及細則的權利，毋須事先通知。如有任何爭議，本公司將保留最終決定權。</p>
    <p>5. 如此條款及細則的中、英文版有所差異，一概以中文版為準。</p>
  </div>
  <div class="terms-en">
    <p class="title">The Cash Coupon Terms and Conditions</p>
    <p>1.&nbsp; The cash coupon is the cash reward of shopping in Mabel’s Nook. Those consumers having purchased $5000 or above in our company every time (be subject to the shopping<br>amount shown on the invoice, calculated on the same invoice as required), and successfully applied for the VIP members of our company, will be presented with HK$500 cash reward.</p>
    <p>2.&nbsp; Each qualified client can use one cash coupon if he purchases for HK$5000 or above every time; for HK$10000 or above can use<br>two cash coupons and so on, no cap, purchase more and more in return.</p>
    <p>3.&nbsp; The using details of cash coupon must be subjected to the company’s related terms restrictions. Mabel’s Nook will not reissue or exchange cash<br>coupons in case of any loss or defacement, or undertake any responsibility.</p>
    <p>4.&nbsp; This company reserves the right to modify, suspend or cancel the above privileges, terms and conditions, without prior notice. In case of disputes, t<br>his company reserves the right to make final decision.</p>
    <p>5. In case of any difference between the Chinese and English versions in the terms and conditions, the Chinese version shall prevail.</p>
  </div>
</section>

<section class="coupon-back">
  <div class="terms-zh">
    <p class="title">現金券條款及細則</p>
    <p>1. 此現金券為本公司(Mabel’s Nook)的購物現金回贈，每次於本公司購物滿港幣$5000或以上(以發票上所示的購物金額為準，並需要在同一張發票內計算)，並需要成功申請成為本公司VIP會員，方可獲贈HK$500 現金回贈。</p>
    <p>2. 每位合格客戶每次購物滿港幣$5000或以上可使用一張現金回贈券一張，購物滿港幣$10000或以上可使用兩張現金回贈券，如此類推，不設上限，多買多回贈。</p>
    <p>3. 現金券的使用細則須受本公司的相關條款限制，現金券如有遺失或損毀，本公司(Mabel’s Nook)概不補發或更換現金券，亦不會<br>承擔任何責任。</p>
    <p>4. 本公司保留隨時修改、暫停或取消以上優惠及其條款及細則的權利，毋須事先通知。如有任何爭議，本公司將保留最終決定權。</p>
    <p>5. 如此條款及細則的中、英文版有所差異，一概以中文版為準。</p>
  </div>
  <div class="terms-en">
    <p class="title">The Cash Coupon Terms and Conditions</p>
    <p>1.&nbsp; The cash coupon is the cash reward of shopping in Mabel’s Nook. Those consumers having purchased $5000 or above in our company every time (be subject to the shopping<br>amount shown on the invoice, calculated on the same invoice as required), and successfully applied for the VIP members of our company, will be presented with HK$500 cash reward.</p>
    <p>2.&nbsp; Each qualified client can use one cash coupon if he purchases for HK$5000 or above every time; for HK$10000 or above can use<br>two cash coupons and so on, no cap, purchase more and more in return.</p>
    <p>3.&nbsp; The using details of cash coupon must be subjected to the company’s related terms restrictions. Mabel’s Nook will not reissue or exchange cash<br>coupons in case of any loss or defacement, or undertake any responsibility.</p>
    <p>4.&nbsp; This company reserves the right to modify, suspend or cancel the above privileges, terms and conditions, without prior notice. In case of disputes, t<br>his company reserves the right to make final decision.</p>
    <p>5. In case of any difference between the Chinese and English versions in the terms and conditions, the Chinese version shall prevail.</p>
  </div>
</section>

<section class="coupon-back">
  <div class="terms-zh">
    <p class="title">現金券條款及細則</p>
    <p>1. 此現金券為本公司(Mabel’s Nook)的購物現金回贈，每次於本公司購物滿港幣$5000或以上(以發票上所示的購物金額為準，並需要在同一張發票內計算)，並需要成功申請成為本公司VIP會員，方可獲贈HK$500 現金回贈。</p>
    <p>2. 每位合格客戶每次購物滿港幣$5000或以上可使用一張現金回贈券一張，購物滿港幣$10000或以上可使用兩張現金回贈券，如此類推，不設上限，多買多回贈。</p>
    <p>3. 現金券的使用細則須受本公司的相關條款限制，現金券如有遺失或損毀，本公司(Mabel’s Nook)概不補發或更換現金券，亦不會<br>承擔任何責任。</p>
    <p>4. 本公司保留隨時修改、暫停或取消以上優惠及其條款及細則的權利，毋須事先通知。如有任何爭議，本公司將保留最終決定權。</p>
    <p>5. 如此條款及細則的中、英文版有所差異，一概以中文版為準。</p>
  </div>
  <div class="terms-en">
    <p class="title">The Cash Coupon Terms and Conditions</p>
    <p>1.&nbsp; The cash coupon is the cash reward of shopping in Mabel’s Nook. Those consumers having purchased $5000 or above in our company every time (be subject to the shopping<br>amount shown on the invoice, calculated on the same invoice as required), and successfully applied for the VIP members of our company, will be presented with HK$500 cash reward.</p>
    <p>2.&nbsp; Each qualified client can use one cash coupon if he purchases for HK$5000 or above every time; for HK$10000 or above can use<br>two cash coupons and so on, no cap, purchase more and more in return.</p>
    <p>3.&nbsp; The using details of cash coupon must be subjected to the company’s related terms restrictions. Mabel’s Nook will not reissue or exchange cash<br>coupons in case of any loss or defacement, or undertake any responsibility.</p>
    <p>4.&nbsp; This company reserves the right to modify, suspend or cancel the above privileges, terms and conditions, without prior notice. In case of disputes, t<br>his company reserves the right to make final decision.</p>
    <p>5. In case of any difference between the Chinese and English versions in the terms and conditions, the Chinese version shall prevail.</p>
  </div>
</section>

<section class="coupon-back">
  <div class="terms-zh">
    <p class="title">現金券條款及細則</p>
    <p>1. 此現金券為本公司(Mabel’s Nook)的購物現金回贈，每次於本公司購物滿港幣$5000或以上(以發票上所示的購物金額為準，並需要在同一張發票內計算)，並需要成功申請成為本公司VIP會員，方可獲贈HK$500 現金回贈。</p>
    <p>2. 每位合格客戶每次購物滿港幣$5000或以上可使用一張現金回贈券一張，購物滿港幣$10000或以上可使用兩張現金回贈券，如此類推，不設上限，多買多回贈。</p>
    <p>3. 現金券的使用細則須受本公司的相關條款限制，現金券如有遺失或損毀，本公司(Mabel’s Nook)概不補發或更換現金券，亦不會<br>承擔任何責任。</p>
    <p>4. 本公司保留隨時修改、暫停或取消以上優惠及其條款及細則的權利，毋須事先通知。如有任何爭議，本公司將保留最終決定權。</p>
    <p>5. 如此條款及細則的中、英文版有所差異，一概以中文版為準。</p>
  </div>
  <div class="terms-en">
    <p class="title">The Cash Coupon Terms and Conditions</p>
    <p>1.&nbsp; The cash coupon is the cash reward of shopping in Mabel’s Nook. Those consumers having purchased $5000 or above in our company every time (be subject to the shopping<br>amount shown on the invoice, calculated on the same invoice as required), and successfully applied for the VIP members of our company, will be presented with HK$500 cash reward.</p>
    <p>2.&nbsp; Each qualified client can use one cash coupon if he purchases for HK$5000 or above every time; for HK$10000 or above can use<br>two cash coupons and so on, no cap, purchase more and more in return.</p>
    <p>3.&nbsp; The using details of cash coupon must be subjected to the company’s related terms restrictions. Mabel’s Nook will not reissue or exchange cash<br>coupons in case of any loss or defacement, or undertake any responsibility.</p>
    <p>4.&nbsp; This company reserves the right to modify, suspend or cancel the above privileges, terms and conditions, without prior notice. In case of disputes, t<br>his company reserves the right to make final decision.</p>
    <p>5. In case of any difference between the Chinese and English versions in the terms and conditions, the Chinese version shall prevail.</p>
  </div>
</section>

<section class="coupon-back">
  <div class="terms-zh">
    <p class="title">現金券條款及細則</p>
    <p>1. 此現金券為本公司(Mabel’s Nook)的購物現金回贈，每次於本公司購物滿港幣$5000或以上(以發票上所示的購物金額為準，並需要在同一張發票內計算)，並需要成功申請成為本公司VIP會員，方可獲贈HK$500 現金回贈。</p>
    <p>2. 每位合格客戶每次購物滿港幣$5000或以上可使用一張現金回贈券一張，購物滿港幣$10000或以上可使用兩張現金回贈券，如此類推，不設上限，多買多回贈。</p>
    <p>3. 現金券的使用細則須受本公司的相關條款限制，現金券如有遺失或損毀，本公司(Mabel’s Nook)概不補發或更換現金券，亦不會<br>承擔任何責任。</p>
    <p>4. 本公司保留隨時修改、暫停或取消以上優惠及其條款及細則的權利，毋須事先通知。如有任何爭議，本公司將保留最終決定權。</p>
    <p>5. 如此條款及細則的中、英文版有所差異，一概以中文版為準。</p>
  </div>
  <div class="terms-en">
    <p class="title">The Cash Coupon Terms and Conditions</p>
    <p>1.&nbsp; The cash coupon is the cash reward of shopping in Mabel’s Nook. Those consumers having purchased $5000 or above in our company every time (be subject to the shopping<br>amount shown on the invoice, calculated on the same invoice as required), and successfully applied for the VIP members of our company, will be presented with HK$500 cash reward.</p>
    <p>2.&nbsp; Each qualified client can use one cash coupon if he purchases for HK$5000 or above every time; for HK$10000 or above can use<br>two cash coupons and so on, no cap, purchase more and more in return.</p>
    <p>3.&nbsp; The using details of cash coupon must be subjected to the company’s related terms restrictions. Mabel’s Nook will not reissue or exchange cash<br>coupons in case of any loss or defacement, or undertake any responsibility.</p>
    <p>4.&nbsp; This company reserves the right to modify, suspend or cancel the above privileges, terms and conditions, without prior notice. In case of disputes, t<br>his company reserves the right to make final decision.</p>
    <p>5. In case of any difference between the Chinese and English versions in the terms and conditions, the Chinese version shall prevail.</p>
  </div>
</section>

</main>
</body>
</html>
```